A SEASON OF EMBERS book cover needed

Hello friends! I'm working toward self-publishing my first novel in the next few months, and I'm looking to have a professional-looking, 6 in x 9 in cover to go along with the ebook release. I’m not looking for much, but the key is that it must look professional. I don’t want decorative fonts, but I also don’t want it to just look like Helvetica or Times New Roman.The text for the cover should be:A TIME FOR GREATNESSKARLIS WILDEI have attached a few images to show you where my head is at. I created a book cover myself on paint that looks horribly amateur, but it draws inspiration from a HPB campaign poster(also attached) where the title of the novel comes from. If you can make that same kind of cover, but make it look professional, that would be amazing! If you have other, simple ideas, I am also very, very open.Attached as well are a couple of simple, recent book covers that I like. That is the kind of thing that I am looking for.If this goes well, I may do a paperback release. In that case, I may need to contact you again for an additional fee to create the rest of the wraparound design. In addition, the book is the first in a projected trilogy, so there may be opportunities for you in the future for sequel covers.About the book: A SEASON OF EMBERS is a gripping, standalone thriller with an exciting take on history, relationships, conspiracy theories, and the current, volatile political state of America. In the present day, new information surrounding the 1963 assassination of Harold P. Brisbane comes to light and Milo Fenwright, a young, best-selling journalist still reconciling his success with his dark past, finds himself more personally connected than he ever could have expected. But the story becomes something even bigger when an assassination attempt on the current demagogic president sends the whole world of journalism into a scramble, and Milo finds himself confronted by an extremely difficult question: Is democracy real, or has it been an illusion fostered by these secretive ‘Stewards of the Union’ since 1776? Travelling across Syria, Canada, and the United States of America, the story becomes more unbelievable—and more personal—as increasingly prominent figures begin to enter Milo’s orbit, intent on keeping their secrets safe by whatever means necessary.

Colors

Designer to choose colors to be used in the design.

Requirements
Must have
• Text
• Simplicity
• Professional look
Should not have
• Cheap fonts
• Complicated images

```html
<!DOCTYPE html>
<html lang="en">
<head>
<meta charset="utf-8">
<title>A Season of Embers — Tomas Reyvik</title>
<link rel="stylesheet" href="https://fonts.googleapis.com/css2?family=Passion+One&family=Montserrat:wght@700;800&display=swap">
<style>
  :root {
    --cover-red: #a1292a;
    --paper: #f3f0e4;
    --navy: #033552;
    --frame-line: #f6f2e6;
  }
  html, body {
    margin: 0;
    padding: 0;
    width: 800px;
    height: 1200px;
    overflow: hidden;
    background: var(--cover-red);
  }
  .book-cover {
    display: block;
    width: 800px;
    height: 1200px;
  }
  .cover-ground { fill: var(--cover-red); }
  .frame-rule { fill: none; stroke: var(--frame-line); stroke-width: 3; }
  .paper-panel { fill: var(--paper); }
  .title-band { fill: var(--navy); }
  .star { fill: var(--navy); }
  .tagline {
    font-family: "Montserrat", sans-serif;
    font-weight: 800;
    font-size: 20px;
    letter-spacing: 0.32em;
    fill: var(--cover-red);
  }
  .title {
    font-family: "Passion One", sans-serif;
    font-weight: 400;
    text-anchor: middle;
  }
  .title-small { font-size: 48px; letter-spacing: 0.06em; }
  .title-large { font-size: 112px; letter-spacing: 0.05em; }
  .title-on-paper { fill: var(--cover-red); }
  .title-on-band { fill: var(--paper); }
  .author-name {
    font-family: "Montserrat", sans-serif;
    font-weight: 700;
    font-size: 24px;
    letter-spacing: 0.36em;
    fill: var(--navy);
    text-anchor: middle;
  }
  .author-rule { stroke-width: 3; }
</style>
</head>
<body>
<svg class="book-cover" viewBox="0 0 800 1200" xmlns="http://www.w3.org/2000/svg" role="img" aria-label="Cover of A Season of Embers by Tomas Reyvik">
  <defs>
    <linearGradient id="rule-fade-left" x1="0" x2="1" y1="0" y2="0">
      <stop offset="0" stop-color="#a1292a" stop-opacity="0"/>
      <stop offset="0.6" stop-color="#a1292a" stop-opacity="1"/>
    </linearGradient>
    <linearGradient id="rule-fade-right" x1="1" x2="0" y1="0" y2="0">
      <stop offset="0" stop-color="#a1292a" stop-opacity="0"/>
      <stop offset="0.6" stop-color="#a1292a" stop-opacity="1"/>
    </linearGradient>
    <polygon id="star-shape" points="0,-8 2.35,-2.47 7.6,-2.47 3.8,0.94 4.7,6.47 0,3.4 -4.7,6.47 -3.8,0.94 -7.6,-2.47 -2.35,-2.47"/>
  </defs>

  <rect class="cover-ground" x="0" y="0" width="800" height="1200"/>
  <rect class="frame-rule" x="48.5" y="48.5" width="703" height="1103"/>
  <rect class="paper-panel" x="68" y="68" width="664" height="1064"/>

  <rect class="title-band" x="0" y="535" width="800" height="265"/>

  <g class="tagline-stars">
    <use href="#star-shape" class="star" x="96" y="97"/>
    <use href="#star-shape" class="star" x="123" y="97"/>
    <use href="#star-shape" class="star" x="150" y="97"/>
    <use href="#star-shape" class="star" x="650" y="97"/>
    <use href="#star-shape" class="star" x="677" y="97"/>
    <use href="#star-shape" class="star" x="704" y="97"/>
  </g>
  <text class="tagline" x="400" y="104" text-anchor="middle">IS DEMOCRACY REAL?</text>

  <text class="title title-small title-on-paper" x="400" y="356">A</text>
  <text class="title title-large title-on-paper" x="400" y="462">SEASON</text>
  <text class="title title-small title-on-band" x="400" y="623">OF</text>
  <text class="title title-large title-on-band" x="400" y="737">EMBERS</text>

  <g class="author-rules">
    <line class="author-rule" x1="85" y1="1096" x2="205" y2="1096" stroke="url(#rule-fade-left)"/>
    <line class="author-rule" x1="85" y1="1104" x2="205" y2="1104" stroke="url(#rule-fade-left)"/>
    <line class="author-rule" x1="85" y1="1112" x2="205" y2="1112" stroke="url(#rule-fade-left)"/>
    <line class="author-rule" x1="595" y1="1096" x2="715" y2="1096" stroke="url(#rule-fade-right)"/>
    <line class="author-rule" x1="595" y1="1104" x2="715" y2="1104" stroke="url(#rule-fade-right)"/>
    <line class="author-rule" x1="595" y1="1112" x2="715" y2="1112" stroke="url(#rule-fade-right)"/>
  </g>
  <text class="author-name" x="404" y="1113">TOMAS REYVIK</text>
</svg>
</body>
</html>
```